Business Card Design Project

looking for business cards with new logo

I am looking to keep with the colors of the logo i posted.  Here are some other details to consider.  I would like my website prominently displayed on the business card with the logo.  my website is www.HavenrockTX.com...it should be spelled this way.

My contact information is:

Daniel P Whitcomb III
Broker/Owner
48391 Cordell Ave., Suite 307
Larkfield, Texas 78461
Office: 737-555-0147
Email:  Daniel@HavenrockTX.com

Thank you
Daniel Whitcomb

```html
<!DOCTYPE html>
<html lang="en">
<head>
<meta charset="utf-8">
<title>Havenrock Realty – Business Card</title>
<link rel="stylesheet" href="https://fonts.googleapis.com/css2?family=Mulish:ital,wght@0,400;0,600;0,700;1,400;1,700&display=swap">
<style>
  :root {
    --page-bg: #e9eaec;
    --card-white: #ffffff;
    --card-navy: #1d3f6c;
    --brand-navy: #1f3f78;
    --accent-blue: #2ba4e3;
    --text-light: #ffffff;
    --mark-grey: #4a4a4a;
  }
  * { box-sizing: border-box; margin: 0; padding: 0; }
  html, body {
    width: 1200px; height: 1200px; overflow: hidden;
    background: var(--page-bg);
    font-family: "Mulish", "Helvetica Neue", Arial, sans-serif;
  }
  .sheet {
    width: 1200px; height: 1200px;
    display: flex; flex-direction: column;
    align-items: center; justify-content: center; gap: 64px;
  }
  .card {
    position: relative;
    width: 900px; height: 514px;
    box-shadow: 0 10px 30px rgba(0,0,0,0.18);
  }
  .card-front { background: var(--card-white); }
  .card-back { background: var(--card-navy); color: var(--text-light); }

  .brand {
    position: absolute; left: 0; right: 0; top: 205px;
    display: flex; align-items: center; justify-content: center; gap: 18px;
  }
  .brand-square { width: 30px; height: 30px; background: var(--accent-blue); }
  .brand-name {
    font-size: 64px; font-weight: 700; color: var(--brand-navy);
    letter-spacing: -0.5px;
  }

  .corner-mark {
    position: absolute; right: 68px; bottom: 58px;
    width: 92px; height: 92px; background: var(--mark-grey);
  }
  .card-back .corner-mark { background: rgba(255,255,255,0.22); }

  .holder { position: absolute; left: 52px; top: 40px; }
  .holder-name {
    font-size: 30px; font-weight: 700; font-style: italic;
    color: var(--accent-blue);
  }
  .holder-title { font-size: 18px; margin-top: 6px; margin-left: 4px; font-style: italic; }

  .contact {
    position: absolute; top: 200px;
    font-size: 19px; line-height: 1.4;
  }
  .contact-phone { left: 52px; }
  .contact-address { left: 482px; }
  .label { color: var(--accent-blue); font-style: italic; }
  .accent { color: var(--accent-blue); font-style: italic; }

  .website {
    position: absolute; left: 24px; width: 560px; bottom: 64px;
    text-align: center; font-size: 24px; font-weight: 600;
    color: var(--accent-blue);
  }
  .website-rule {
    position: absolute; left: 24px; width: 560px; bottom: 50px;
    height: 2px; background: var(--text-light);
  }
</style>
</head>
<body>
<main class="sheet">
  <section class="card card-front" aria-label="Card front">
    <div class="brand">
      <span class="brand-square"></span>
      <span class="brand-name">Havenrock Realty</span>
    </div>
    <div class="corner-mark"></div>
  </section>

  <section class="card card-back" aria-label="Card back">
    <div class="holder">
      <p class="holder-name">Daniel P Whitcomb III</p>
      <p class="holder-title">Broker/Owner</p>
    </div>
    <div class="contact contact-phone">
      <p><span class="label">Office</span>: 737-555-0147</p>
      <p><span class="label">Email</span>:&nbsp; Daniel@HavenrockTX.com</p>
    </div>
    <div class="contact contact-address">
      <p><span class="accent">48391</span> Cordell Ave., Suite 307</p>
      <p>Larkfield, Texas 78461</p>
    </div>
    <p class="website">www.HavenrockTX.com</p>
    <div class="website-rule"></div>
    <div class="corner-mark"></div>
  </section>
</main>
</body>
</html>
```